The Cedarline Newsletter For My Monthly Investment Newsletters

I'm looking to create two beautiful newsletter template for my new financial planning and investment firm. I keep my newsletters short and sweet as I feel less is more. One newsletter is for investment updates - I send that to clients and prospects. The other is more of an update for clients only.

I'm going to be using Mailchimp & Constant Contact so please make sure I can use that template there.

My newsletter typically goes out monthly. There are two versions - one for clients and one for prospects. Sometimes, information is applicable for clients only.

The newsletter brief should have the month and year in it like
The Cedarline Newsletter: March 2020.

The other can be

The Cedarline Update: March 2020 (for more administrative announcements).

Target Market(s)

Investors

Industry/Entity Type

Investment Advisory

Font styles to use
Sans Serif

Colors

Designer to choose colors to be used in the design.

Requirements
Must have
• Clean
• professional
• Modern feel
• Less is more.
• Colors should match and be in sync my logo.
• I'm going to be using Mailchimp & Constant Contact so please make sure I can use that template there.
Nice to have
• Please follow the must haves

```html
<!DOCTYPE html>
<html lang="en">
<head>
<meta charset="utf-8">
<title>The Cedarline Newsletter</title>
<link href="https://fonts.googleapis.com/css2?family=Montserrat:wght@200;300;600;700&family=Questrial&display=swap" rel="stylesheet">
<style>
  :root {
    --hero-top: #6f5a45;
    --hero-mid: #3a3843;
    --hero-bottom: #1d2233;
    --white: #ffffff;
    --ink: #111111;
    --body-ink: #222222;
    --brand-blue: #135d87;
    --band-blue: #1f7799;
    --footer-dark: #1b1c1e;
    --rule: #6a6a6a;
    --card-shadow: rgba(0, 0, 0, 0.22);
    --social: #2f5f8f;
  }
  * { margin: 0; padding: 0; box-sizing: border-box; }
  html, body { width: 786px; height: 1200px; overflow: hidden; background: var(--white); }
  body { position: relative; font-family: "Questrial", sans-serif; color: var(--body-ink); }

  .hero {
    position: absolute; left: 0; top: 0; width: 786px; height: 410px;
    background: linear-gradient(180deg, var(--hero-top) 0%, #5a4c43 22%, var(--hero-mid) 52%, var(--hero-bottom) 100%);
  }
  .brand {
    position: absolute; display: flex; align-items: center; gap: 8px;
    font-family: "Montserrat", sans-serif; font-weight: 600; font-size: 20px; color: var(--white);
  }
  .brand-mark { width: 14px; height: 14px; border-radius: 50%; background: currentColor; }
  .hero .brand { left: 64px; top: 44px; }
  .issue-date {
    position: absolute; left: 0; top: 176px; width: 786px; text-align: center;
    font-family: "Montserrat", sans-serif; font-weight: 200; font-size: 46px; color: var(--white); letter-spacing: 0.5px;
  }

  .card {
    position: absolute; top: 459px; width: 261px; height: 355px; background: var(--white);
    box-shadow: 0 6px 10px var(--card-shadow); text-align: center;
  }
  .card-left { left: 109px; }
  .card-right { left: 417px; }
  .card-photo { position: absolute; left: 14px; top: 10px; width: 233px; height: 168px; }
  .photo-advisor { background: linear-gradient(135deg, #c9c2b8 0%, #2b3850 45%, #1c2436 100%); }
  .photo-chart { background: linear-gradient(160deg, #0e1014 0%, #1d2a2a 50%, #4a5a8a 80%, #b9a77a 100%); }
  .card-title {
    position: absolute; left: 0; top: 200px; width: 100%;
    font-family: "Montserrat", sans-serif; font-weight: 600; font-size: 19px; color: var(--ink);
  }
  .card-text { position: absolute; left: 20px; top: 233px; width: 221px; font-size: 10px; line-height: 18px; color: var(--body-ink); }
  .card-button {
    position: absolute; left: 72px; top: 301px; width: 118px; height: 30px; border-radius: 15px;
    background: var(--brand-blue); color: var(--white); font-size: 9.5px; line-height: 30px; text-transform: uppercase;
  }

  .meeting-band { position: absolute; left: 0; top: 857px; width: 786px; height: 124px; background: var(--band-blue); color: var(--white); }
  .meeting-title { position: absolute; left: 74px; top: 32px; font-family: "Montserrat", sans-serif; font-weight: 600; font-size: 18px; }
  .meeting-text { position: absolute; left: 70px; top: 64px; font-size: 9.5px; line-height: 19px; }
  .meeting-button {
    position: absolute; left: 498px; top: 47px; width: 148px; height: 31px; border: 1px solid var(--white); border-radius: 16px;
    font-size: 9.5px; line-height: 29px; text-align: center; text-transform: uppercase;
  }

  .footer { position: absolute; left: 0; top: 981px; width: 786px; height: 219px; background: var(--footer-dark); }
  .footer .brand { left: 0; top: 64px; width: 786px; justify-content: center; color: #3f87b5; }
  .social { position: absolute; left: 337px; top: 120px; display: flex; gap: 9px; }
  .social-link { width: 22px; height: 22px; background: var(--social); }
  .footer-rule { position: absolute; left: 0; top: 171px; width: 786px; height: 1px; background: var(--rule); }
  .copyright { position: absolute; left: 0; top: 189px; width: 786px; text-align: center; font-size: 10px; color: var(--white); }
</style>
</head>
<body>
  <header class="hero" role="img" aria-label="Dusk city skyline with twin towers under a cloudy sky">
    <div class="brand"><span class="brand-mark"></span>The Cedarline LLC</div>
    <div class="issue-date">Feb,08,2020</div>
  </header>

  <section class="card card-left">
    <div class="card-photo photo-advisor" role="img" aria-label="Advisor in a suit giving a thumbs up"></div>
    <h2 class="card-title">For Financial Planning</h2>
    <p class="card-text">Integer vitae tempor dui, at placerat odio. Aenean ante nisl, suscipit ac arcu lobortis, malesuada tempus mi</p>
    <div class="card-button">Read More</div>
  </section>

  <section class="card card-right">
    <div class="card-photo photo-chart" role="img" aria-label="Tablet screen showing market charts"></div>
    <h2 class="card-title">For Investment Firm</h2>
    <p class="card-text">Integer vitae tempor dui, at placerat odio. Aenean ante nisl, suscipit ac arcu lobortis, malesuada tempus mi</p>
    <div class="card-button">Read More</div>
  </section>

  <section class="meeting-band">
    <h2 class="meeting-title">Schedule A Meeting</h2>
    <p class="meeting-text">Morbi sit amet aliquam nibh. Phasellus vitae dapibus magna, sit amet cursus neque.<br>Praesent efficitur vitae odio ut laoreet. Nullam sed odio</p>
    <div class="meeting-button">Schedule A Meeting</div>
  </section>

  <footer class="footer">
    <div class="brand"><span class="brand-mark"></span>The Cedarline LLC</div>
    <div class="social">
      <span class="social-link" aria-label="Social link"></span>
      <span class="social-link" aria-label="Social link"></span>
      <span class="social-link" aria-label="Social link"></span>
      <span class="social-link" aria-label="Social link"></span>
    </div>
    <div class="footer-rule"></div>
    <p class="copyright">©&nbsp; Copyright 2020 The Cedarline</p>
  </footer>
</body>
</html>
```